my project is brownie with no sugar under brand name tundle bites (tundle bites brownie )
we are looking to have amazing and attractive label design for whom like eating brownie but they concern about them sugar intake
we need to have all the information on label size as attached

```html
<!DOCTYPE html>
<html lang="en">
<head>
<meta charset="UTF-8">
<title>Tundle Bites Brownie – Wrapper Label</title>
<link href="https://fonts.googleapis.com/css2?family=Comic+Neue:wght@700&family=Great+Vibes&display=swap" rel="stylesheet">
<style>
  :root {
    --backdrop: #ececec;
    --wrap-light: #cf6a2c;
    --wrap-mid: #9c4318;
    --wrap-dark: #5c200c;
    --crimp: #d5773a;
    --accent-gold: #f0a51c;
    --accent-red: #e4231c;
    --accent-green: #7cc242;
    --ink-light: #ffffff;
    --photo-main: #6b3a1f;
    --photo-light: #a9734a;
  }
  * { margin: 0; padding: 0; box-sizing: border-box; }
  html, body { width: 1200px; height: 800px; overflow: hidden; }
  body { background: var(--backdrop); position: relative; font-family: "Comic Neue", sans-serif; }

  .wrapper { position: absolute; left: 50px; top: 210px; width: 1100px; height: 380px; }
  .wrapper svg { position: absolute; inset: 0; }

  .brand-name {
    position: absolute; left: 120px; top: 145px; width: 260px;
    font-weight: 700; font-size: 54px; line-height: 0.95;
    color: var(--accent-gold); text-transform: uppercase; letter-spacing: 1px;
  }
  .brand-dot {
    position: absolute; left: 330px; top: 212px; width: 22px; height: 22px;
    border-radius: 50%; background: var(--accent-gold);
  }
  .product-type {
    position: absolute; left: 400px; top: 40px;
    font-weight: 700; font-size: 30px; line-height: 1; color: var(--accent-gold);
  }
  .product-name {
    position: absolute; left: 385px; top: 120px;
    font-family: "Great Vibes", cursive; font-size: 120px; line-height: 1;
    color: var(--accent-red); white-space: nowrap;
  }
  .product-claim {
    position: absolute; left: 600px; top: 270px;
    font-weight: 700; font-size: 32px; line-height: 1; color: var(--accent-green);
  }
  .brownie-photo {
    position: absolute; left: 775px; top: 30px; width: 140px; height: 125px; border-radius: 10px;
    background: linear-gradient(160deg, var(--photo-light), var(--photo-main));
  }
  .sugar-badge {
    position: absolute; left: 930px; top: 30px; width: 80px; height: 80px;
    border: 2px dashed var(--ink-light); border-radius: 50%;
    display: flex; flex-direction: column; align-items: center; justify-content: center;
    color: var(--ink-light); font-weight: 700; font-size: 13px; line-height: 1.15; text-align: center;
  }
</style>
</head>
<body>
  <div class="wrapper">
    <svg width="1100" height="380" viewBox="0 0 1100 380">
      <defs>
        <linearGradient id="wrap-fill" x1="0" y1="0" x2="1" y2="0">
          <stop offset="0" stop-color="var(--wrap-light)"/>
          <stop offset="0.5" stop-color="var(--wrap-mid)"/>
          <stop offset="1" stop-color="var(--wrap-dark)"/>
        </linearGradient>
        <pattern id="halftone" width="10" height="10" patternUnits="userSpaceOnUse">
          <circle cx="5" cy="5" r="1.6" fill="#000" opacity="0.12"/>
        </pattern>
        <pattern id="ridges" width="10" height="380" patternUnits="userSpaceOnUse">
          <rect width="5" height="380" fill="#000" opacity="0.08"/>
        </pattern>
        <pattern id="teeth-left" width="20" height="20" patternUnits="userSpaceOnUse">
          <polygon points="0,10 20,0 20,20" fill="var(--crimp)"/>
        </pattern>
        <pattern id="teeth-right" width="20" height="20" patternUnits="userSpaceOnUse">
          <polygon points="0,0 20,10 0,20" fill="var(--wrap-dark)"/>
        </pattern>
      </defs>
      <rect x="0" y="0" width="20" height="380" fill="url(#teeth-left)"/>
      <rect x="1080" y="0" width="20" height="380" fill="url(#teeth-right)"/>
      <rect class="wrapper-body" x="20" y="0" width="1060" height="380" fill="url(#wrap-fill)"/>
      <rect x="20" y="0" width="1060" height="380" fill="url(#halftone)"/>
      <rect class="crimp-left" x="20" y="0" width="60" height="380" fill="url(#ridges)"/>
      <rect class="crimp-right" x="1020" y="0" width="60" height="380" fill="url(#ridges)"/>
      <line x1="80" y1="0" x2="80" y2="380" stroke="#000" stroke-opacity="0.15" stroke-width="2"/>
      <line x1="1020" y1="0" x2="1020" y2="380" stroke="#000" stroke-opacity="0.15" stroke-width="2"/>
    </svg>

    <div class="brand-name">Tundle<br>Bites</div>
    <span class="brand-dot"></span>

    <div class="product-type">chocolate bar</div>
    <div class="brownie-photo" role="img" aria-label="Photo of stacked chocolate brownie squares dusted with sugar"></div>
    <div class="product-name">Brownie</div>
    <div class="product-claim">with stevia</div>

    <div class="sugar-badge"><span>100%</span><span>no sugar</span></div>
  </div>
</body>
</html>
```